Waste Oil Filter collection & disposal

Basically I need a 1 page website for the business called Brenmoor Waste Solutions.
We are a environmental service provider and we collect and dispose of waste oil filters to protect the environment from hazardous waste oil products.

This is the link to our current website: www.brenmoorwaste.co.nz

we want it to look fresh and better than our current website. we may potentially look at getting a new logo designed and are open to ideas/designs if you have any.

Industry/Entity Type

Business

Logo Text

Brenmoor Waste Solutions

Number of Pages Required

1 page

Requirements
Must have
• same colours as current website.
• description of what service we provide please refer to leaflet attached

```html
<!DOCTYPE html>
<html lang="en">
<head>
<meta charset="utf-8">
<title>Brenmoor Waste Solutions</title>
<link href="https://fonts.googleapis.com/css2?family=Open+Sans:ital,wght@0,400;0,600;0,700;1,400&display=swap" rel="stylesheet">
<style>
:root{
  --green:#3db53d;
  --dark:#333333;
  --darker:#222222;
  --ink:#333333;
  --muted:#555555;
  --band:#efefef;
  --panel:#f2f2f2;
  --white:#ffffff;
  --line:#999999;
}
*{box-sizing:border-box;margin:0;padding:0}
html,body{width:1200px;height:2459px;overflow:hidden}
body{font-family:"Open Sans",Arial,sans-serif;color:var(--ink);background:var(--white);position:relative}
.container{position:absolute;left:133px;width:934px}
.site-header{position:absolute;top:0;left:0;width:1200px;height:85px}
.brand{position:absolute;left:133px;top:28px;display:flex;align-items:center;gap:8px;font-weight:700;font-size:14px;color:var(--dark)}
.brand-mark{width:22px;height:22px;background:var(--green);border-radius:50%}
.contact{position:absolute;top:33px;font-size:20px;color:var(--green);display:flex;align-items:center;gap:8px}
.contact.email{left:646px}
.contact.phone{left:936px}
.main-nav{position:absolute;top:85px;left:0;width:1200px;height:41px;background:var(--dark)}
.main-nav ul{list-style:none;position:absolute;left:133px;top:0;display:flex;height:41px}
.main-nav li{font-size:13px;font-weight:600;text-transform:uppercase;color:#dddddd;padding:0 23px;line-height:41px}
.main-nav li.active{background:var(--darker);color:var(--white);padding:0 20px}
.hero{position:absolute;top:126px;left:0;width:1200px;height:489px;background:linear-gradient(135deg,#6f7570 0%,#3f4a45 40%,#2e6b5a 70%,#4d5650 100%)}
.hero-arrow{position:absolute;top:230px}
.intro h1{position:absolute;top:690px;font-size:23px;line-height:32px;font-weight:600;color:var(--green);text-transform:uppercase;text-align:center;width:934px}
.intro p{position:absolute;top:754px;font-size:15px;line-height:21px;color:var(--ink);text-align:center;width:934px}
.intro-photo{position:absolute;left:360px;top:818px;width:479px;height:303px;background:linear-gradient(135deg,#3a3a40,#8a8c90 45%,#2d3550 75%,#5a4a48)}
.process{position:absolute;top:1201px;left:0;width:1200px;height:408px;background:var(--band)}
.process h2{position:absolute;top:66px;width:1200px;text-align:center;font-size:31px;font-weight:700;color:var(--green)}
.process .lead{position:absolute;top:110px;width:1200px;text-align:center;font-size:17px;line-height:26px;color:var(--ink)}
.process-line{position:absolute;top:223px;left:193px;width:812px;height:1px;background:var(--line)}
.step{position:absolute;top:190px;width:140px;margin-left:-70px;text-align:center}
.step-icon{width:66px;height:66px;border-radius:50%;background:var(--dark);margin:0 auto;display:flex;align-items:center;justify-content:center}
.step-label{font-size:17px;line-height:20px;margin-top:20px;color:var(--ink)}
.quote{position:absolute;top:1690px;width:296px;text-align:center}
.quote-box{height:119px;border:1px solid #aaaaaa;background:var(--white);display:flex;align-items:center;justify-content:center;padding:0 22px;font-size:17px;line-height:24px;font-weight:600;position:relative}
.quote-tail{position:absolute;left:130px;bottom:-21px}
.quote cite{display:block;margin-top:31px;font-size:16px;font-style:italic}
.feature{position:absolute;top:1944px;left:133px;width:934px;height:319px}
.feature-text{position:absolute;left:0;top:0;width:467px;height:319px;background:var(--panel);padding:33px 31px}
.feature-text h3{font-size:22px;line-height:30px;font-weight:600;color:var(--green)}
.feature-text p{margin-top:14px;font-size:12.5px;line-height:21px;color:var(--ink)}
.btn{display:inline-block;margin-top:22px;background:var(--green);color:var(--white);font-size:13px;font-weight:700;text-transform:uppercase;width:119px;height:38px;line-height:38px;text-align:center}
.feature-photo{position:absolute;left:467px;top:0;width:467px;height:319px;background:linear-gradient(180deg,#3f5c3b 0%,#6d8467 45%,#c8cfcc 65%,#2f8a5a 80%,#6b6d66 100%)}
.site-footer{position:absolute;top:2344px;left:0;width:1200px;height:115px;background:var(--dark)}
.footer-links{position:absolute;left:133px;top:34px;font-size:12px;color:#cccccc}
.footer-links span{margin:0 8px;color:#999999}
.copyright{position:absolute;left:133px;top:62px;font-size:12px;color:#bbbbbb}
.social{position:absolute;top:44px;width:25px;height:25px;border-radius:50%}
.social.one{left:1007px;background:#3b5998}
.social.two{left:1040px;background:#1da1f2}
</style>
</head>
<body>
<header class="site-header">
  <div class="brand"><span class="brand-mark"></span>Brenmoor Waste Solutions</div>
  <div class="contact email">
    <svg width="18" height="14" viewBox="0 0 18 14"><rect width="18" height="14" rx="1" fill="#3db53d"/><path d="M1 1l8 7 8-7" stroke="#fff" stroke-width="1.6" fill="none"/></svg>
    info@brenmoorwaste.co.nz
  </div>
  <div class="contact phone">
    <svg width="16" height="16" viewBox="0 0 24 24"><path fill="#3db53d" d="M6.6 10.8a15.1 15.1 0 006.6 6.6l2.2-2.2c.3-.3.7-.4 1-.2 1.1.4 2.3.6 3.6.6.6 0 1 .4 1 1V20c0 .6-.4 1-1 1A17 17 0 013 4c0-.6.4-1 1-1h3.5c.6 0 1 .4 1 1 0 1.3.2 2.5.6 3.6.1.3 0 .7-.2 1z"/></svg>
    06 555 0142
  </div>
</header>

<nav class="main-nav">
  <ul>
    <li class="active">Home</li>
    <li>About Us</li>
    <li>Services</li>
    <li>Gallery</li>
    <li>Contact Us</li>
  </ul>
</nav>

<section class="hero" role="img" aria-label="Workshop with stacked bricks of crushed oil filters on a green processing bench">
  <svg class="hero-arrow" style="left:46px" width="14" height="20" viewBox="0 0 14 20"><path d="M11 2L3 10l8 8" stroke="#fff" stroke-width="3.5" fill="none"/></svg>
  <svg class="hero-arrow" style="left:1140px" width="14" height="20" viewBox="0 0 14 20"><path d="M3 2l8 8-8 8" stroke="#fff" stroke-width="3.5" fill="none"/></svg>
</section>

<section class="intro">
  <h1 class="container">Brenmoor Waste Solutions Ltd specialize in the collection &amp; disposal of oil / fuel filters, servicing the lower North Island on a monthly cycle</h1>
  <p class="container">We offer a cost effective environmentally friendly system for the collection and disposal of waste oil filters helping minimise contamination of landfills keeping your industry compliant.</p>
  <div class="intro-photo" role="img" aria-label="Close view of a compressed block of used oil filters"></div>
</section>

<section class="process">
  <h2>THE PROCESS</h2>
  <p class="lead">Filters are collected and transported back to the processing plant.<br>At the processing plant they are:</p>
  <div class="process-line"></div>
  <div class="step" style="left:193px">
    <div class="step-icon"><svg width="24" height="28" viewBox="0 0 24 28"><path d="M12 2C12 2 4 12 4 18a8 8 0 0016 0C20 12 12 2 12 2z" fill="#fff"/></svg></div>
    <div class="step-label">Drained</div>
  </div>
  <div class="step" style="left:356px">
    <div class="step-icon"><svg width="26" height="26" viewBox="0 0 26 26"><path d="M2 3h22l-9 10v10l-4-3v-7z" fill="#fff"/></svg></div>
    <div class="step-label">Sorted</div>
  </div>
  <div class="step" style="left:518px">
    <div class="step-icon"><svg width="28" height="28" viewBox="0 0 28 28"><path d="M11 6C11 6 4 14 4 19a7 7 0 0014 0C18 14 11 6 11 6z" fill="#fff"/><path d="M21 2s-4 5-4 8a4 4 0 008 0c0-3-4-8-4-8z" fill="#fff"/></svg></div>
    <div class="step-label">Drained again</div>
  </div>
  <div class="step" style="left:680px">
    <div class="step-icon"><svg width="30" height="30" viewBox="0 0 30 30" stroke="#fff" stroke-width="3" fill="none" stroke-linecap="round"><path d="M12 8l-4 4a4 4 0 000 6"/><path d="M18 22l4-4a4 4 0 000-6"/><path d="M11 4v3M5 11h3M19 26v-3M25 19h-3M7 6l2 2M23 24l-2-2"/></svg></div>
    <div class="step-label">Crushed into bricks</div>
  </div>
  <div class="step" style="left:842px">
    <div class="step-icon"><svg width="30" height="30" viewBox="0 0 30 30" fill="#fff"><path d="M15 9s-6 7-6 11a6 6 0 0012 0c0-4-6-11-6-11z"/><path d="M8 2s-3 4-3 6a3 3 0 006 0c0-2-3-6-3-6z"/><path d="M22 2s-3 4-3 6a3 3 0 006 0c0-2-3-6-3-6z"/></svg></div>
    <div class="step-label">Drained a third time</div>
  </div>
  <div class="step" style="left:1005px">
    <div class="step-icon"><svg width="30" height="30" viewBox="0 0 30 30" stroke="#fff" stroke-width="3.2" fill="none"><path d="M24 12A10 10 0 006 10"/><path d="M6 18a10 10 0 0018 2"/><path d="M4 4v7h7" stroke-width="0" fill="#fff"/><path d="M26 26v-7h-7" stroke-width="0" fill="#fff"/></svg></div>
    <div class="step-label">Stacked ready for Metal Recycling</div>
  </div>
</section>

<section class="quotes">
  <figure class="quote" style="left:133px">
    <blockquote class="quote-box">"each used oi l filterhas on aver age, more than quarter of alitre of used motor oil "
      <svg class="quote-tail" width="34" height="22" viewBox="0 0 34 22"><path d="M0 0L17 20 34 0" fill="#fff" stroke="#aaa"/><rect x="1" y="-2" width="32" height="3" fill="#fff"/></svg>
    </blockquote>
    <cite>- GreenCycle Agency</cite>
  </figure>
  <figure class="quote" style="left:451px">
    <blockquote class="quote-box">"recyclin g engine oil protects the environment and conserves energy resources "
      <svg class="quote-tail" width="34" height="22" viewBox="0 0 34 22"><path d="M0 0L17 20 34 0" fill="#fff" stroke="#aaa"/><rect x="1" y="-2" width="32" height="3" fill="#fff"/></svg>
    </blockquote>
    <cite>- Oi l Recycl ing</cite>
  </figure>
  <figure class="quote" style="left:770px">
    <blockquote class="quote-box">"one litre of used oil can contam-inate onemillion litres of water "
      <svg class="quote-tail" width="34" height="22" viewBox="0 0 34 22"><path d="M0 0L17 20 34 0" fill="#fff" stroke="#aaa"/><rect x="1" y="-2" width="32" height="3" fill="#fff"/></svg>
    </blockquote>
    <cite>- Harbourview District Council</cite>
  </figure>
</section>

<section class="feature">
  <div class="feature-text">
    <h3>Brenmoor Waste Solutions Ltd service the Lower North Island and specialise in the collection &amp; disposal of oil &amp; fuel filters</h3>
    <p>We are passionate about doing our bit in keeping New Zealand Clean and Green. We offer a cost effective system for the collection and disposal of waste oil filters. Our processes are environmentally friendly and minimise the contamination of landfills. We keep your industry compliant.</p>
    <span class="btn">Contact Us</span>
  </div>
  <div class="feature-photo" role="img" aria-label="Green and white collection truck parked in front of trees"></div>
</section>

<footer class="site-footer">
  <div class="footer-links">Home<span>|</span>About Us<span>|</span>Services<span>|</span>Gallery<span>|</span>Contact Us</div>
  <div class="copyright">Copyright &copy; 2017 Brenmoor Waste Solutions Ltd. &nbsp;All rights reserved.</div>
  <span class="social one" aria-label="Social link"></span>
  <span class="social two" aria-label="Social link"></span>
</footer>
</body>
</html>
```